Optometrist/Eye Care Clinic Business card with new logo attached

We are a small, independent eye care clinic in Canada. We have recently updated our logo (as attached), and would like a professional, modern and health care oriented business card to highlight our office details and our optometrist. We'd like to incorporate the blue colours as seen on our logo.

Target Market(s)

demographic: age 35-65 male/female equal

Industry/Entity Type

Health Care

Contact Information for Business Card

Name of clinic: "Marrow Bend Eye Care Optometry"

Font styles to use
Sans Serif

Colors
0355a3

Requirements
Must have
• our website: marrowbendeyecare.com
• Dr Lena Quorvik
• Optometrist
• 217-392 E Halvering Ave
• Vancouver BC V6R 3J8
• P: 604-319-2058
• E: info@marrowbendeyecare.com
Nice to have
• front side: logo/name of clinic as seen on logo attached and website
• backside: logo on the left side, and name/title/address/phone/email

```html
<!DOCTYPE html>
<html lang="en">
<head>
<meta charset="utf-8">
<title>Marrow Bend Eye Care Optometry – Business Card</title>
<link href="https://fonts.googleapis.com/css2?family=Open+Sans:wght@400;600&display=swap" rel="stylesheet">
<style>
  :root {
    --page: #ffffff;
    --card-light: #f7fbfe;
    --card-edge: #cde4f3;
    --sky: #4fb3e0;
    --sky-pale: #a9dbf3;
    --navy: #1b3a6b;
    --brand: #1a6f92;
    --ink: #222222;
    --icon: #2a9fe0;
    --rule: #4aa3df;
    --bar: #2b7fc4;
  }
  * { margin: 0; padding: 0; box-sizing: border-box; }
  html, body { width: 1200px; height: 900px; overflow: hidden; background: var(--page); }
  body { position: relative; font-family: "Open Sans", Arial, sans-serif; }

  .card {
    position: absolute;
    width: 692px;
    height: 394px;
    overflow: hidden;
    background: radial-gradient(ellipse at 45% 40%, var(--card-light) 0%, #eaf4fb 45%, var(--card-edge) 100%);
    box-shadow: 8px 8px 10px rgba(0, 0, 0, 0.45);
  }
  .card--front { left: 43px; top: 38px; }
  .card--back { left: 392px; top: 472px; width: 688px; }

  .card__swoosh { position: absolute; left: 0; top: 0; width: 100%; height: 100%; }

  .brand { position: absolute; text-align: center; color: var(--brand); font-weight: 400; }
  .brand__mark { display: block; margin: 0 auto 14px; border-radius: 50%; background: var(--brand); }
  .brand__line { display: block; line-height: 1; white-space: nowrap; }
  .brand__line--name { font-size: 27px; letter-spacing: 4px; }
  .brand__line--care { font-size: 33px; letter-spacing: 5px; margin-top: 4px; }
  .brand__line--type { font-size: 16px; letter-spacing: 7px; margin-top: 6px; }

  .card--front .brand { left: 197px; top: 100px; width: 300px; }
  .card--front .brand__mark { width: 96px; height: 96px; }

  .web-bar {
    position: absolute; left: 31px; top: 324px; width: 296px; height: 40px;
    background: linear-gradient(90deg, var(--bar) 0%, #5aa3da 55%, rgba(255,255,255,0) 100%);
    color: #ffffff; font-size: 21px; line-height: 40px; padding-left: 18px;
  }

  .card--back .brand { left: 60px; top: 98px; width: 290px; }
  .card--back .brand__mark { width: 104px; height: 104px; margin-bottom: 16px; }
  .card--back .brand__line--name { font-size: 24px; }
  .card--back .brand__line--care { font-size: 30px; }
  .card--back .brand__line--type { font-size: 15px; }

  .person { position: absolute; right: 28px; top: 52px; text-align: right; color: var(--ink); }
  .person__name { font-size: 37px; font-weight: 400; line-height: 1.05; }
  .person__title { font-size: 19px; line-height: 1.2; }
  .person__rule { position: absolute; left: 390px; top: 125px; width: 273px; height: 1px; background: var(--rule); }

  .contact { position: absolute; right: 30px; top: 148px; list-style: none; color: var(--ink); }
  .contact__item { display: flex; justify-content: flex-end; align-items: center; height: 49px; font-size: 16px; }
  .contact__item svg { width: 32px; height: 32px; margin-left: 4px; flex: none; }
  .contact__item--web span { letter-spacing: 1px; }
  .contact__item--address { align-items: center; height: 52px; }
  .contact__address { text-align: right; line-height: 1.45; }
  .contact__address small { display: block; font-size: 13.5px; letter-spacing: -0.2px; }
</style>
</head>
<body>

<section class="card card--front" aria-label="Card front">
  <svg class="card__swoosh" viewBox="0 0 692 394" aria-hidden="true">
    <path d="M0,120 C60,60 170,15 315,0 C170,10 60,50 0,100 Z" fill="var(--sky)"/>
    <path d="M0,175 C50,90 160,25 315,0 C170,18 60,80 0,140 Z" fill="var(--navy)"/>
    <path d="M0,205 C45,110 160,30 315,0 C165,28 55,110 0,185 Z" fill="#ffffff"/>
    <path d="M692,190 C600,290 500,360 378,394 L692,394 Z" fill="var(--sky-pale)"/>
    <path d="M692,215 C610,300 510,365 378,394 L692,394 Z" fill="var(--sky)"/>
    <path d="M692,245 C620,320 520,375 378,394 C530,370 630,320 692,280 Z" fill="var(--navy)"/>
    <path d="M692,192 C610,285 510,360 378,394 C515,358 615,285 692,232 Z" fill="#ffffff"/>
  </svg>

  <div class="brand">
    <span class="brand__mark"></span>
    <span class="brand__line brand__line--name">MARROW BEND</span>
    <span class="brand__line brand__line--care">EYE CARE</span>
    <span class="brand__line brand__line--type">OPTOMETRY</span>
  </div>

  <div class="web-bar">marrowbendeyecare.com</div>
</section>

<section class="card card--back" aria-label="Card back">
  <svg class="card__swoosh" viewBox="0 0 688 394" aria-hidden="true">
    <path d="M0,190 C40,290 150,360 313,394 L0,394 Z" fill="var(--sky-pale)"/>
    <path d="M0,230 C45,310 150,365 313,394 L0,394 Z" fill="var(--sky)"/>
    <path d="M0,215 C45,300 150,360 313,394 C160,375 50,320 0,265 Z" fill="var(--navy)"/>
    <path d="M0,188 C40,285 150,355 313,394 C150,365 40,300 0,222 Z" fill="#ffffff"/>
  </svg>

  <div class="brand">
    <span class="brand__mark"></span>
    <span class="brand__line brand__line--name">MARROW BEND</span>
    <span class="brand__line brand__line--care">EYE CARE</span>
    <span class="brand__line brand__line--type">OPTOMETRY</span>
  </div>

  <div class="person">
    <h1 class="person__name">Dr. Lena Quorvik</h1>
    <p class="person__title">Optometrist</p>
  </div>
  <div class="person__rule"></div>

  <ul class="contact">
    <li class="contact__item">
      <span>604 319 2058</span>
      <svg viewBox="0 0 32 32" aria-hidden="true">
        <path d="M3,12 C3,5 29,5 29,12 L29,14 L22,14 L22,10 C18,9 14,9 10,10 L10,14 L3,14 Z" fill="var(--icon)"/>
        <path d="M8,16 L11,12 L21,12 L24,16 L26,27 L6,27 Z" fill="var(--icon)"/>
        <g fill="#ffffff">
          <rect x="11" y="17" width="2" height="2"/><rect x="15" y="17" width="2" height="2"/><rect x="19" y="17" width="2" height="2"/>
          <rect x="11" y="21" width="2" height="2"/><rect x="15" y="21" width="2" height="2"/><rect x="19" y="21" width="2" height="2"/>
        </g>
      </svg>
    </li>
    <li class="contact__item">
      <span>info@marrowbendeyecare.com</span>
      <svg viewBox="0 0 32 32" aria-hidden="true">
        <rect x="3" y="8" width="26" height="17" fill="var(--icon)"/>
        <path d="M3,8 L16,18 L29,8 M3,25 L12,15 M29,25 L20,15" fill="none" stroke="#ffffff" stroke-width="1.5"/>
      </svg>
    </li>
    <li class="contact__item contact__item--web">
      <span>marrowbendeyecare.com</span>
      <svg viewBox="0 0 32 32" aria-hidden="true">
        <g fill="none" stroke="var(--icon)" stroke-width="1.6">
          <circle cx="16" cy="16" r="12"/>
          <ellipse cx="16" cy="16" rx="5.5" ry="12"/>
          <path d="M4,16 H28 M6,10 H26 M6,22 H26 M16,4 V28"/>
        </g>
      </svg>
    </li>
    <li class="contact__item contact__item--address">
      <div class="contact__address">
        217-392 E Halvering Ave
        <small>Vancouver, British Columbia V6R 3J8</small>
      </div>
      <svg viewBox="0 0 32 32" aria-hidden="true">
        <path d="M16,30 C10,21 6,16 6,11 A10,10 0 0 1 26,11 C26,16 22,21 16,30 Z" fill="var(--icon)"/>
        <circle cx="16" cy="11" r="3.5" fill="#ffffff"/>
      </svg>
    </li>
  </ul>
</section>

</body>
</html>
```